Market Research firm needs updated business cards with new logo

We need the logo to be included somewhere on the card (attached). We would also like the phrases "Independent, Objective, Comprehensive" and "Research You Can Trust" somewhere on the card. Front or back. Our colors are hex codes 6075a7, e48d25 and 5a5b5b. Though you are certainly not limited to those shades, whatever you produce should coordinate with them. I have also attached our favicon. Feel free to use it in your design, but please do not use it to replace the full logo.

Contact Information for Business Card

see project description

Other font styles liked:
• Open Sans

Requirements
Must have
• the logo
• We use Open Sans font

```html
<!DOCTYPE html>
<html lang="en">
<head>
<meta charset="utf-8">
<title>Norland Research Business Card</title>
<link rel="stylesheet" href="https://fonts.googleapis.com/css2?family=Open+Sans:wght@400;600&family=Libre+Baskerville:ital@1&display=swap">
<style>
  :root {
    --stage: #2a2a2c;
    --card-dark: #161618;
    --card-light: #f7f7f7;
    --orange: #e48d25;
    --slate: #5a5b5b;
    --blue-grey: #6075a7;
    --silver: #b9bcc2;
  }
  * { margin: 0; padding: 0; box-sizing: border-box; }
  html, body { width: 1200px; height: 900px; overflow: hidden; }
  body {
    background: var(--stage);
    font-family: "Open Sans", sans-serif;
    display: flex;
    flex-direction: column;
    align-items: center;
    justify-content: center;
    gap: 44px;
  }
  .card {
    width: 640px;
    height: 366px;
    border-radius: 28px;
    position: relative;
    box-shadow: 0 12px 30px rgba(0,0,0,.45);
  }
  .card-back {
    background: var(--card-dark);
    display: flex;
    flex-direction: column;
    align-items: center;
    justify-content: center;
  }
  .brand {
    display: flex;
    align-items: center;
    gap: 12px;
    color: var(--orange);
    font-weight: 600;
    white-space: nowrap;
  }
  .brand-dot {
    border-radius: 50%;
    background: var(--orange);
    flex: none;
  }
  .card-back .brand { font-size: 50px; letter-spacing: .5px; }
  .card-back .brand-dot { width: 26px; height: 26px; }
  .tagline {
    margin-top: 58px;
    text-align: center;
    font-size: 17px;
    line-height: 1.4;
  }
  .tagline-values { color: var(--orange); }
  .tagline-promise { color: var(--silver); }

  .card-front {
    background: var(--card-light);
    display: flex;
    align-items: center;
    padding: 0 40px 0 52px;
  }
  .card-front .brand { font-size: 27px; width: 300px; margin-top: -40px; }
  .card-front .brand-dot { width: 15px; height: 15px; }
  .contact { margin-left: 28px; color: var(--slate); }
  .person-name { font-size: 27px; font-weight: 400; letter-spacing: .5px; line-height: 1.1; }
  .job-title {
    font-family: "Libre Baskerville", serif;
    font-style: italic;
    color: var(--orange);
    font-size: 14px;
    margin-bottom: 18px;
  }
  .contact-list { list-style: none; font-size: 17px; line-height: 1.6; }
  .contact-list li { display: flex; align-items: center; gap: 10px; }
  .contact-list svg { width: 14px; height: 14px; fill: var(--orange); flex: none; }
  .address { font-size: 17px; line-height: 1.5; margin-top: 14px; }
</style>
</head>
<body>
  <section class="card card-back">
    <div class="brand"><span class="brand-dot"></span>Norland Research</div>
    <p class="tagline">
      <span class="tagline-values">Independent, Objective, Comprehensive</span><br>
      <span class="tagline-promise">Research You Can Trust</span>
    </p>
  </section>

  <section class="card card-front">
    <div class="brand"><span class="brand-dot"></span>Norland Research</div>
    <div class="contact">
      <h1 class="person-name">YOUR NAME</h1>
      <p class="job-title">Job Title</p>
      <ul class="contact-list">
        <li>
          <svg viewBox="0 0 16 16" aria-hidden="true"><path d="M3 2h3l1.5 3.5-2 1.2a8 8 0 0 0 3.8 3.8l1.2-2L14 10v3a1 1 0 0 1-1 1A11 11 0 0 1 2 3a1 1 0 0 1 1-1z"/></svg>
          000 000 0000
        </li>
        <li>
          <svg viewBox="0 0 16 16" aria-hidden="true"><path d="M1 3h14v10H1z M1 3l7 5 7-5" fill="var(--orange)" stroke="var(--card-light)" stroke-width="1"/></svg>
          youremail@xyz.com
        </li>
        <li>
          <svg viewBox="0 0 16 16" aria-hidden="true"><circle cx="8" cy="8" r="6.5" fill="none" stroke="var(--orange)" stroke-width="1.3"/><path d="M1.5 8h13M8 1.5c-3 3.5-3 9.5 0 13M8 1.5c3 3.5 3 9.5 0 13" fill="none" stroke="var(--orange)" stroke-width="1.1"/></svg>
          www.yourwebsite.com
        </li>
      </ul>
      <p class="address">0000, Anywehre, Somewhere<br>City. ST 0000</p>
    </div>
  </section>
</body>
</html>
```